TK Drafting

Simple Design - Logo is done (from this site). Logo on one side - Back Side an image or outline of a house blue print - My name, phone, email, website url. Prefer the traditional Architectural style of letters -

Target Market(s)

Customers who need a floor plan redesigned for renovations or realtors who want a floor plan for marketing their listings

Industry/Entity Type

Architecture

Contact Information for Business Card

Colin Varga - Name
318-542-6604 - Phone
tkdraftingco@mailvane.com
www.tkdraftingco.net

Font styles to use
Other font styles liked:
• Architecture writing -

Colors
0555a3
3276b5
85acd3

Requirements
Must have
• Logo that is attached. I like an indigo blue color for the background or a royal blue - gray logo OR - white and clean with the logo on one side and the same color gray lettering on the other side
Nice to have
• some sort of image that shows a residential blue print. It may not be possible on this small of a card though.
Should not have
• Nothing cartoonish.

```html
<!DOCTYPE html>
<html lang="en">
<head>
<meta charset="utf-8">
<title>TK Drafting — Business Card</title>
<link rel="stylesheet" href="https://fonts.googleapis.com/css2?family=Montserrat:wght@400;500;600&display=swap">
<style>
  :root {
    --canvas-bg: #1b1b1e;
    --card-violet: #4b2a84;
    --card-violet-deep: #432577;
    --plan-line: #5a3a93;
    --mark-grey: #b9b8c2;
    --text-white: #f2f0f7;
    --rule-grey: #8f85ad;
  }
  * { box-sizing: border-box; margin: 0; padding: 0; }
  html, body {
    width: 1200px;
    height: 900px;
    overflow: hidden;
    background: var(--canvas-bg);
    font-family: "Montserrat", sans-serif;
  }
  .sheet {
    width: 1200px;
    height: 900px;
    display: flex;
    flex-direction: column;
    align-items: center;
    justify-content: center;
    gap: 44px;
  }
  .card {
    position: relative;
    width: 640px;
    height: 366px;
    background: var(--card-violet);
    overflow: hidden;
  }

  /* Front: name + contact side */
  .card-front {
    display: flex;
    align-items: center;
  }
  .front-brand {
    width: 290px;
    display: flex;
    justify-content: flex-end;
    align-items: center;
    gap: 12px;
    padding-right: 34px;
  }
  .brand-square {
    width: 18px;
    height: 18px;
    background: var(--mark-grey);
  }
  .brand-name {
    color: var(--mark-grey);
    font-weight: 500;
    font-size: 28px;
    letter-spacing: 0.08em;
  }
  .front-divider {
    width: 1px;
    height: 126px;
    background: var(--rule-grey);
  }
  .front-contact {
    padding-left: 36px;
    color: var(--text-white);
  }
  .contact-name {
    font-weight: 600;
    font-size: 21px;
    letter-spacing: 0.06em;
    text-transform: uppercase;
    margin-bottom: 18px;
  }
  .contact-list { list-style: none; }
  .contact-item {
    display: flex;
    align-items: center;
    gap: 10px;
    font-size: 16px;
    font-weight: 400;
    line-height: 1.55;
  }
  .contact-icon { width: 17px; height: 17px; flex: none; }

  /* Back: plan background + brand */
  .card-back { background: var(--card-violet-deep); }
  .plan-field {
    position: absolute;
    inset: 0;
    background: linear-gradient(135deg, var(--card-violet) 0%, var(--card-violet-deep) 55%, var(--plan-line) 100%);
  }
  .back-brand {
    position: absolute;
    inset: 0;
    display: flex;
    align-items: center;
    justify-content: center;
    gap: 20px;
  }
  .back-brand .brand-square { width: 30px; height: 30px; }
  .back-brand .brand-name { font-size: 52px; }
</style>
</head>
<body>
<main class="sheet">
  <section class="card card-front" aria-label="Business card front">
    <div class="front-brand">
      <span class="brand-square"></span>
      <span class="brand-name">TK Drafting</span>
    </div>
    <div class="front-divider"></div>
    <div class="front-contact">
      <h1 class="contact-name">Colin Varga</h1>
      <ul class="contact-list">
        <li class="contact-item">
          <svg class="contact-icon" viewBox="0 0 20 20" aria-hidden="true">
            <circle cx="10" cy="10" r="9" fill="none" stroke="#f2f0f7" stroke-width="1.4"/>
            <path d="M7 5.5 L8.6 5.5 L9.2 8 L8.2 8.8 Q9.2 11 11.2 11.8 L12 10.8 L14.5 11.4 L14.5 13 Q10.5 13.5 8 11 Q6 8.8 7 5.5 Z" fill="#f2f0f7"/>
          </svg>
          <span>318-542-6604</span>
        </li>
        <li class="contact-item">
          <svg class="contact-icon" viewBox="0 0 20 20" aria-hidden="true">
            <circle cx="10" cy="10" r="9" fill="none" stroke="#f2f0f7" stroke-width="1.4"/>
            <rect x="5.5" y="6.8" width="9" height="6.4" fill="none" stroke="#f2f0f7" stroke-width="1.2"/>
            <path d="M5.5 6.8 L10 10.4 L14.5 6.8" fill="none" stroke="#f2f0f7" stroke-width="1.2"/>
          </svg>
          <span>tkdraftingco@mailvane.com</span>
        </li>
        <li class="contact-item">
          <svg class="contact-icon" viewBox="0 0 20 20" aria-hidden="true">
            <circle cx="10" cy="10" r="9" fill="none" stroke="#f2f0f7" stroke-width="1.4"/>
            <circle cx="10" cy="10" r="5" fill="none" stroke="#f2f0f7" stroke-width="1"/>
            <ellipse cx="10" cy="10" rx="2.2" ry="5" fill="none" stroke="#f2f0f7" stroke-width="1"/>
            <path d="M5 10 H15" stroke="#f2f0f7" stroke-width="1"/>
          </svg>
          <span>www.tkdraftingco.net</span>
        </li>
      </ul>
    </div>
  </section>

  <section class="card card-back" aria-label="Business card back">
    <div class="plan-field" role="img" aria-label="Faint residential floor plan drawing in violet tones covering the card"></div>
    <div class="back-brand">
      <span class="brand-square"></span>
      <span class="brand-name">TK Drafting</span>
    </div>
  </section>
</main>
</body>
</html>
```